Web site for radio show

I've got a radio show starting on VandorFM and need a web site for it. I am familiar with WordPress, so I'd like to get a design for a WordPress-based web site for the show.

I'm also posting a logo project to be done at the same time.

The best radio show web site I've seen is the Lumen Tuesday site (www.lumentuesday.example). That's a good model but I don't want to start with that much complexity and content. The initial site that I'd like you to design would have the following parts:
- Upcoming shows
- Past shows (including links to authors, their web sites, and their books)
- Chirply feed
- Blog
- About
- ...and anything else you think would be necessary

For colors, I'd like it to be consistent with my personal web site: www.haldanecraftworks.example

Target Market(s)

The target market for this show is mid- to upper-level managers

Industry/Entity Type

Radio

Requirements
Must have
• The project has to proceed in (at least) two stages: a first rough layout, and a second finished design. Whether you want a third stage in between with look and feel options is up to you.

```html
<!DOCTYPE html>
<html lang="en">
<head>
<meta charset="utf-8">
<title>VandorFM – Radio Show</title>
<link href="https://fonts.googleapis.com/css2?family=Open+Sans:wght@300;400;600;700;800&display=swap" rel="stylesheet">
<style>
:root{
  --bg-dark:#1d1a17;
  --bg-mid:#3b342d;
  --page:#f2f2f0;
  --white:#ffffff;
  --ink:#2b2b2b;
  --muted:#8a8a8a;
  --line:#dcdcdc;
  --red:#e2342b;
  --panel-dark:#262626;
  --footer:#1b1b1b;
}
*{margin:0;padding:0;box-sizing:border-box}
html,body{width:839px;height:1200px;overflow:hidden}
body{
  position:relative;
  font-family:"Open Sans",Arial,sans-serif;
  color:var(--ink);
  background:radial-gradient(ellipse 520px 420px at 70% 8%,#6b6157 0%,var(--bg-mid) 45%,var(--bg-dark) 100%);
}
.brand{position:absolute;left:56px;top:22px;font-size:30px;font-weight:300;color:var(--white);letter-spacing:1px}
.countdown{position:absolute;right:56px;top:10px;height:52px;display:flex;background:rgba(20,20,20,.75)}
.countdown .label{width:64px;display:flex;align-items:center;justify-content:center;text-align:center;font-size:8px;font-weight:700;color:var(--white);border-right:1px solid #444;line-height:1.3;padding:0 6px}
.countdown .unit{width:44px;display:flex;flex-direction:column;align-items:center;justify-content:center;border-right:1px solid #444;color:var(--white)}
.countdown .unit b{font-size:17px;font-weight:700;line-height:1}
.countdown .unit span{font-size:6.5px;color:#aaa;margin-top:4px;letter-spacing:.5px}
.countdown .more{width:52px;background:var(--red);color:var(--white);font-size:28px;font-weight:300;display:flex;align-items:center;justify-content:center}

.page{position:absolute;left:56px;top:86px;width:727px;height:912px;background:var(--page)}
.nav{height:36px;background:var(--white);display:flex;align-items:center;padding-left:28px;border-bottom:1px solid var(--line)}
.nav a{font-size:8.5px;font-weight:700;color:#444;text-decoration:none;margin-right:30px;height:36px;display:flex;align-items:center;gap:5px}
.nav a.active{color:var(--red);border-bottom:2px solid var(--red)}

.hero{position:absolute;left:28px;top:76px;width:426px;height:318px;background:linear-gradient(160deg,#5b6c78 0%,#2d3238 55%,#15181b 100%)}
.hero h1{position:absolute;left:20px;bottom:26px;color:var(--white);font-size:29px;font-weight:700;line-height:1.15}
.pager{position:absolute;left:28px;top:400px;width:426px;height:8px;background:#d2d2d2}
.pager i{position:absolute;left:0;top:0;width:120px;height:8px;background:#9a9a9a}

.upcoming{position:absolute;left:468px;top:76px;width:231px;height:318px;background:var(--white)}
.section-head{display:flex;justify-content:space-between;align-items:center;height:30px;border-bottom:1px solid var(--line);position:relative}
.section-head h2{font-size:8.5px;font-weight:800;color:#333;letter-spacing:.3px}
.section-head h2::after{content:"";position:absolute;left:0;bottom:-1px;width:48px;height:2px;background:var(--red)}
.section-head .link{font-size:6.5px;color:var(--muted);font-weight:600;display:flex;align-items:center;gap:4px}
.upcoming .section-head{padding:0 10px}
.upcoming .section-head h2::after{left:10px}
.gig{display:flex;height:68px;border-bottom:1px solid #ececec;align-items:center;padding-left:10px}
.gig .date{width:40px;height:56px;background:var(--red);color:var(--white);display:flex;flex-direction:column;align-items:center;justify-content:center}
.gig .date b{font-size:19px;font-weight:700;line-height:1}
.gig .date span{font-size:7px;font-weight:600;margin-top:3px}
.gig .info{padding-left:12px}
.gig .info h3{font-size:8px;font-weight:800;color:var(--red)}
.gig .info p{font-size:7px;color:var(--muted);margin-top:3px;display:flex;align-items:center;gap:3px}

.featured{position:absolute;left:28px;top:420px;width:426px}
.cards{display:flex;gap:16px;margin-top:16px}
.card{width:205px}
.card .photo{height:127px}
.card h3{font-size:9px;font-weight:800;color:#333;margin-top:8px;line-height:1.3}
.card p{font-size:7px;color:var(--muted);margin-top:5px;line-height:1.45}
.card .meta{display:flex;justify-content:space-between;font-size:6.5px;color:var(--muted);font-weight:600;margin-top:8px;padding-top:6px;border-top:1px solid var(--line)}
.tiles{display:flex;gap:16px;margin-top:36px}
.tile{width:205px;height:148px;background:var(--white);padding:6px}
.tile .photo{height:112px}
.tile .caption{text-align:center;font-size:8px;font-weight:700;color:#333;margin-top:9px}

.video{position:absolute;left:468px;top:420px;width:231px}
.player{margin-top:16px;height:140px;background:#111;border:4px solid #2c2c2c;display:flex;align-items:center;justify-content:center}

.discography{position:absolute;left:468px;top:612px;width:231px}
.album{margin-top:16px;height:168px;background:linear-gradient(180deg,#d9e06a 0%,#c7d241 100%)}
.album-caption{background:var(--panel-dark);padding:8px 10px}
.album-caption b{display:block;font-size:8.5px;font-weight:800;color:var(--white)}
.album-caption span{font-size:7px;color:#aaa}

.footer{position:absolute;left:56px;top:1014px;width:727px;height:186px;background:var(--footer);display:flex;padding:18px 28px 0;gap:30px;color:#9a9a9a}
.footer h4{font-size:8.5px;font-weight:800;color:var(--white);padding-bottom:7px;border-bottom:1px solid #333;margin-bottom:10px;position:relative}
.footer h4::after{content:"";position:absolute;left:0;bottom:-1px;width:40px;height:2px;background:var(--red)}
.footer .col{width:200px}
.footer p{font-size:7px;line-height:1.55}
.news-item{margin-bottom:12px}
.news-item b{display:block;font-size:8px;color:var(--white);font-weight:700}
.news-item span{font-size:6.5px;color:#777}
.social{display:flex;gap:8px}
.social i{width:28px;height:28px;background:#2e2e2e;display:block}
</style>
</head>
<body>
<header>
  <div class="brand">VANDORFM</div>
  <div class="countdown">
    <div class="label">NEXT EVENT IN</div>
    <div class="unit"><b>12</b><span>DAYS</span></div>
    <div class="unit"><b>19</b><span>HOURS</span></div>
    <div class="unit"><b>48</b><span>MINUTES</span></div>
    <div class="unit"><b>27</b><span>SECONDS</span></div>
    <div class="more">+</div>
  </div>
</header>

<main class="page">
  <nav class="nav">
    <a href="#"><svg width="9" height="8" viewBox="0 0 9 8"><path d="M4.5 0L9 4H7.5V8H5.5V5.5H3.5V8H1.5V4H0Z" fill="#444"/></svg>HOME</a>
    <a href="#" class="active">UPCOMING SHOWS</a>
    <a href="#">PAST SHOWS</a>
    <a href="#">ABOUT</a>
    <a href="#">VIDEOS</a>
    <a href="#">GALLERY</a>
    <a href="#">AUDIO</a>
  </nav>

  <section class="hero" role="img" aria-label="Radio studio microphone in front of a mixing desk">
    <h1>Live Show<br>We Love you .....</h1>
  </section>
  <div class="pager"><i></i></div>

  <aside class="upcoming">
    <div class="section-head"><h2>UPCOMING SHOWS</h2><span class="link">
      <svg width="8" height="8" viewBox="0 0 8 8"><rect x=".5" y="1.5" width="7" height="6" fill="none" stroke="#8a8a8a"/><path d="M.5 3.5H7.5" stroke="#8a8a8a"/></svg>CALENDAR</span></div>
    <div class="gig"><div class="date"><b>11</b><span>OCT</span></div><div class="info"><h3>JONAH VALE</h3><p><svg width="6" height="7" viewBox="0 0 6 7"><path d="M3 0A3 3 0 0 1 6 3C6 5 3 7 3 7S0 5 0 3A3 3 0 0 1 3 0Z" fill="#8a8a8a"/></svg>LEDGERLINE | LONDON</p></div></div>
    <div class="gig"><div class="date"><b>17</b><span>OCT</span></div><div class="info"><h3>COPPER ANTLER</h3><p><svg width="6" height="7" viewBox="0 0 6 7"><path d="M3 0A3 3 0 0 1 6 3C6 5 3 7 3 7S0 5 0 3A3 3 0 0 1 3 0Z" fill="#8a8a8a"/></svg>THE ASHFORD | LONDON</p></div></div>
    <div class="gig"><div class="date"><b>6</b><span>NOV</span></div><div class="info"><h3>THE VELVET PAIR</h3><p><svg width="6" height="7" viewBox="0 0 6 7"><path d="M3 0A3 3 0 0 1 6 3C6 5 3 7 3 7S0 5 0 3A3 3 0 0 1 3 0Z" fill="#8a8a8a"/></svg>THE REGENT ROOM | LONDON</p></div></div>
    <div class="gig"><div class="date"><b>12</b><span>DEC</span></div><div class="info"><h3>JULIET'S ECHO</h3><p><svg width="6" height="7" viewBox="0 0 6 7"><path d="M3 0A3 3 0 0 1 6 3C6 5 3 7 3 7S0 5 0 3A3 3 0 0 1 3 0Z" fill="#8a8a8a"/></svg>THE CELLAR VAULT | CAMDEN</p></div></div>
  </aside>

  <section class="featured">
    <div class="section-head"><h2>FEATURED</h2><span class="link">▤ ALL NEWS</span></div>
    <div class="cards">
      <article class="card">
        <div class="photo" role="img" aria-label="Glowing red on-air sign" style="background:linear-gradient(180deg,#2a1a16 0%,#a3241b 50%,#2a1a16 100%)"></div>
        <h3>Kavah Brings African Music to Brooklyn Studio Compilation</h3>
        <p>A warm new compilation gathers street rhythms, late sessions and bright guitars recorded live over one busy summer week.</p>
        <div class="meta"><span>15 SEP 2013</span><span>READ MORE ›</span></div>
      </article>
      <article class="card">
        <div class="photo" role="img" aria-label="Singer wearing studio headphones" style="background:linear-gradient(135deg,#cfcfcf 0%,#8d8d8d 60%,#5a5a5a 100%)"></div>
        <h3>Song Premiere: Clara Wynmoor – "Ember Tide" (Nordhal Remix)</h3>
        <p>The remix slows the original ballad into a glowing ambient piece with layered strings, soft choirs and a patient pulse.</p>
        <div class="meta"><span>15 SEP 2013</span><span>READ MORE ›</span></div>
      </article>
    </div>
    <div class="tiles">
      <article class="tile">
        <div class="photo" role="img" aria-label="Crowd at a concert under stage lights" style="background:linear-gradient(180deg,#3a3f4a 0%,#14161b 100%)"></div>
        <div class="caption">Paul Orin Farewell Tour</div>
      </article>
      <article class="tile">
        <div class="photo" role="img" aria-label="Band performing against red stage light" style="background:linear-gradient(180deg,#c23a4c 0%,#5e1420 100%)"></div>
        <div class="caption">Lattice Models</div>
      </article>
    </div>
  </section>

  <section class="video">
    <div class="section-head"><h2>VIDEO</h2></div>
    <div class="player">
      <svg width="40" height="30" viewBox="0 0 40 30"><rect width="40" height="30" rx="4" fill="#3a3a3a"/><path d="M16 8L26 15L16 22Z" fill="#fff"/></svg>
    </div>
  </section>

  <section class="discography">
    <div class="section-head"><h2>DISCOGRAPHY</h2><span class="link">▤ ALL ALBUMS</span></div>
    <div class="album" role="img" aria-label="Album cover: four band members on a lime green background"></div>
    <div class="album-caption"><b>THE LIME RECORD</b><span>Vintage Band</span></div>
  </section>
</main>

<footer class="footer">
  <div class="col">
    <h4>ABOUT US</h4>
    <p>Our weekly show meets the leaders, authors and makers shaping modern work. Every episode brings honest talk, useful ideas and good music for busy managers who still love to listen.</p>
  </div>
  <div class="col">
    <h4>NEWS</h4>
    <div class="news-item"><b>Discovery of the Week: The Lark Parade</b><span>15 OCT 2013 | 0 COMMENTS</span></div>
    <div class="news-item"><b>Make it easy to live well longer</b><span>15 OCT 2013 | 0 COMMENTS</span></div>
  </div>
  <div class="col">
    <h4>FOLLOW US</h4>
    <div class="social" aria-label="Social links including Chirply"><i></i><i></i><i></i></div>
  </div>
</footer>
</body>
</html>
```